Business Card & Letterhead Design

We a financial advice company based in Australia. We provide advice to wealthy farmers.

We are changing our business name FROM Palomar Financial TO Bluegate Wealth and we need a new letterhead and double sided business card design

Attached is designs from our previous branding (Palomar Financial) as it includes all the details we require on the new Bluegate Wealth business cards and letterhead.

```html
<!DOCTYPE html>
<html lang="en">
<head>
<meta charset="utf-8">
<title>Bluegate Wealth – Business Card</title>
<link href="https://fonts.googleapis.com/css2?family=Source+Sans+3:wght@400;700&display=swap" rel="stylesheet">
<style>
  :root {
    --page: #ffffff;
    --card: #5f6b73;
    --ink: #ffffff;
  }
  * { margin: 0; padding: 0; box-sizing: border-box; }
  html, body {
    width: 1200px;
    height: 1000px;
    overflow: hidden;
    background: var(--page);
    font-family: "Source Sans 3", "Myriad Pro", Arial, sans-serif;
    color: var(--ink);
  }
  .card {
    position: absolute;
    left: 68px;
    top: 205px;
    width: 1062px;
    height: 590px;
    background: var(--card);
  }
  .brand {
    position: absolute;
    left: 100px;
    top: 175px;
    width: 426px;
    text-align: center;
  }
  .brand-mark { display: block; margin: 0 auto; }
  .brand-name {
    margin-top: 8px;
    font-size: 34px;
    font-weight: 400;
    letter-spacing: 1.5px;
    line-height: 1;
    white-space: nowrap;
  }
  .details {
    position: absolute;
    left: 603px;
    top: 52px;
  }
  .tagline {
    font-size: 32px;
    font-weight: 700;
    line-height: 40px;
    letter-spacing: -0.3px;
  }
  .person { margin-top: 50px; }
  .person-name {
    font-size: 37px;
    font-weight: 700;
    line-height: 42px;
  }
  .person-role, .contact {
    font-size: 29px;
    font-weight: 400;
    line-height: 40px;
  }
  .person-role sup { font-size: 15px; vertical-align: 12px; }
  .contact { margin-top: 30px; }
</style>
</head>
<body>
  <div class="card">
    <div class="brand">
      <svg class="brand-mark" width="116" height="116" viewBox="0 0 116 116" aria-hidden="true">
        <circle cx="58" cy="58" r="54" fill="none" stroke="#ffffff" stroke-width="3.5"/>
      </svg>
      <div class="brand-name">BLUEGATE WEALTH</div>
    </div>

    <div class="details">
      <p class="tagline">'Financial peace of mind'</p>
      <div class="person">
        <p class="person-name">Tom Reid</p>
        <p class="person-role">B.Ag.Ec. Dip F.P. CFP<sup>®</sup></p>
        <p class="person-role">Managing Director</p>
        <p class="person-role">Authorised Representative</p>
      </div>
      <div class="contact">
        <p>(07) 3555 0182</p>
        <p>(07) 3555 0247</p>
        <p>0400 555 318</p>
        <p>tom@palomarfinancial.com.au</p>
        <p>www.palomarfinancial.com.au</p>
      </div>
    </div>
  </div>
</body>
</html>
```